Business Cards, Stationary, Fax, Envelopes
Larkspur Valley Wellness Pharmacy and Home Care
Professional
Dale Corvin, PharmD
President
418 Quarry Lane
Phillipsburg, KS 67492-2741
dcorvin@larkspurvalleyrx.example
www.larkspurvalleyrx.example
Our logo is the one with the Blue/Green Rx/Sun symbol. The additional logo provided is to be used ONLY for the back of the business card (read back of business card section).
We have not introduced the new logo to our business yet, so fonts are still changable.
The fonts that the attached logo uses are Versailles LT Bold, Versailles LT and Helvetica NeueLT Std. HOWEVER, we would love to consider other types of fonts if you have ideas that might look better, please try them.
The "Pharmacy and Home Care" could be in black if that looked better than gray for your design.
Thank you!
On the back of the card, please use the round emblem that says PHARMACY AND HOME CARE EXPERTS and then replace the middle of the emblem with our logo Rx/Sun symbol. So this is: Our symbol with the PHARMACY AND HOME CARE EXPERTS surrounding it. Please disregard the Larkspur Valley Wellness part of this particular logo. Thank you!
This is the emblem for the BACK OF THE CARD - please see brief for instructions.

```html
<!DOCTYPE html>
<html lang="en">
<head>
<meta charset="utf-8">
<title>Larkspur Valley Wellness – Stationery Set</title>
<link href="https://fonts.googleapis.com/css2?family=Cormorant+Garamond:wght@700&family=Open+Sans:wght@400;600&display=swap" rel="stylesheet">
<style>
:root{
  --board:#2c2f33;
  --board-light:#3a3e43;
  --paper:#ffffff;
  --paper-shade:#eef1f4;
  --blue:#1f62ad;
  --blue-deep:#0e3d78;
  --blue-light:#5b9ad6;
  --green:#3f9a3c;
  --ink:#333a42;
  --grey:#8a929b;
}
*{margin:0;padding:0;box-sizing:border-box}
html,body{width:1200px;height:206px;overflow:hidden}
body{background:radial-gradient(ellipse at 50% 40%,var(--board-light),var(--board));position:relative;font-family:"Open Sans",Arial,sans-serif;color:var(--ink)}
.piece{position:absolute;background:var(--paper);box-shadow:0 1px 3px rgba(0,0,0,.5);overflow:hidden}
.wordmark{display:flex;align-items:center;gap:3px}
.wordmark .dot{border-radius:50%;background:var(--blue);flex:none}
.wordmark .name{font-family:"Cormorant Garamond",Georgia,serif;font-weight:700;color:var(--blue);line-height:1}
.small{font-size:3px;line-height:1.4;color:var(--grey)}
.wave{position:absolute;left:0;bottom:0;width:100%}
/* brand block on board */
.brand-block{position:absolute;left:12px;top:12px}
.brand-block .dot{width:18px;height:18px}
.brand-block .name{font-size:11px;color:var(--paper)}
.brand-block .tag{font-size:4px;color:#c9d3dd;margin:4px 0 0 22px}
/* business cards */
.card{width:58px;height:34px}
.card .wordmark{position:absolute;left:4px;top:5px}
.card .dot{width:7px;height:7px}
.card .name{font-size:4.5px}
.card.back{background:linear-gradient(160deg,var(--blue-light),var(--blue) 55%,var(--blue-deep))}
.card.back .emblem{position:absolute;left:21px;top:9px;width:16px;height:16px;border-radius:50%;border:1.5px solid var(--paper)}
/* letterhead & fax */
.sheet{width:126px;height:185px;top:11px}
.sheet .wordmark{position:absolute;left:8px;top:8px}
.sheet .dot{width:10px;height:10px}
.sheet .name{font-size:6px}
.sheet .contact{position:absolute;right:8px;top:8px;text-align:right}
.fax-title{position:absolute;left:8px;top:26px;font-size:7px;font-weight:600;color:var(--blue)}
.fax-table{position:absolute;left:8px;top:38px;width:110px;border-collapse:collapse;font-size:3.5px;color:var(--ink)}
.fax-table td{border-bottom:.5px solid #c8cfd6;height:7px}
/* slips */
.slip{width:115px;height:20px}
.slip .wordmark{position:absolute;left:5px;top:5px}
.slip .dot{width:8px;height:8px}
.slip .name{font-size:5px}
/* envelopes */
.envelope{width:170px;height:58px}
.envelope .wordmark{position:absolute;left:6px;top:5px}
.envelope .dot{width:8px;height:8px}
.envelope .name{font-size:5px}
.flap{position:absolute;left:0;top:0;width:100%;height:100%}
/* folders */
.folder{width:122px;height:185px;top:11px}
.folder.closed{background:linear-gradient(170deg,var(--blue-light),var(--blue) 40%,var(--blue-deep))}
.folder.closed .wordmark{position:absolute;left:34px;top:82px;flex-direction:column;gap:4px}
.folder.closed .dot{width:22px;height:22px;background:var(--paper)}
.folder.closed .name{font-size:6px;color:var(--paper)}
.folder.open{width:184px;background:linear-gradient(90deg,var(--paper) 49.6%,var(--paper-shade) 50%,var(--paper))}
.pocket{position:absolute;left:0;bottom:0;width:100%;height:62px}
.pocket-card{position:absolute;left:22px;bottom:30px;width:44px;height:26px;background:var(--paper);box-shadow:0 1px 2px rgba(0,0,0,.3)}
.pocket-card .wordmark{position:absolute;left:3px;top:4px}
.pocket-card .dot{width:6px;height:6px}
.pocket-card .name{font-size:3.5px}
</style>
</head>
<body>

<div class="brand-block">
  <div class="wordmark"><span class="dot"></span><span class="name">Larkspur Valley Wellness</span></div>
  <div class="tag">Pharmacy and Home Care</div>
</div>

<!-- business cards -->
<div class="piece card" style="left:12px;top:96px">
  <div class="wordmark"><span class="dot"></span><span class="name">Larkspur Valley Wellness</span></div>
  <div class="small" style="position:absolute;left:4px;top:16px">Dale Corvin, PharmD<br>President</div>
</div>
<div class="piece card back" style="left:76px;top:96px"><div class="emblem"></div></div>
<div class="piece card" style="left:12px;top:140px">
  <div class="small" style="position:absolute;left:4px;top:5px">418 Quarry Lane<br>Phillipsburg, KS 67492-2741<br>dcorvin@larkspurvalleyrx.example</div>
  <svg class="wave" viewBox="0 0 100 20" preserveAspectRatio="none" height="10"><path d="M0 8 Q50 -2 100 8 V20 H0Z" fill="var(--blue)"/></svg>
</div>
<div class="piece card back" style="left:76px;top:140px"><div class="emblem"></div></div>

<!-- letterhead -->
<div class="piece sheet" style="left:185px">
  <div class="wordmark"><span class="dot"></span><span class="name">Larkspur Valley Wellness</span></div>
  <div class="contact small">418 Quarry Lane<br>Phillipsburg, KS 67492-2741<br>www.larkspurvalleyrx.example</div>
  <svg class="wave" viewBox="0 0 100 20" preserveAspectRatio="none" height="26"><path d="M0 6 Q50 -4 100 6 V20 H0Z" fill="var(--blue-light)"/><path d="M0 10 Q50 2 100 10 V20 H0Z" fill="var(--blue)"/></svg>
</div>

<!-- fax -->
<div class="piece sheet" style="left:320px">
  <div class="wordmark"><span class="dot"></span><span class="name">Larkspur Valley Wellness</span></div>
  <div class="fax-title">FAX</div>
  <table class="fax-table">
    <tr><td>To</td><td>From</td></tr>
    <tr><td>Fax</td><td>Pages</td></tr>
    <tr><td>Date</td><td>Re</td></tr>
  </table>
  <svg class="wave" viewBox="0 0 100 20" preserveAspectRatio="none" height="26"><path d="M0 6 Q50 -4 100 6 V20 H0Z" fill="var(--blue-light)"/><path d="M0 10 Q50 2 100 10 V20 H0Z" fill="var(--blue)"/></svg>
</div>

<!-- compliment slips -->
<div class="piece slip" style="left:460px;top:96px">
  <div class="wordmark"><span class="dot"></span><span class="name">Larkspur Valley Wellness</span></div>
</div>
<div class="piece slip" style="left:460px;top:122px">
  <div class="small" style="position:absolute;left:5px;top:6px">tcorvin · www.larkspurvalleyrx.example</div>
  <svg class="wave" viewBox="0 0 100 20" preserveAspectRatio="none" height="6"><path d="M0 6 Q50 -2 100 6 V20 H0Z" fill="var(--blue)"/></svg>
</div>
<div class="piece slip" style="left:460px;top:150px;height:40px">
  <div class="wordmark"><span class="dot"></span><span class="name">Larkspur Valley Wellness</span></div>
  <svg class="wave" viewBox="0 0 100 20" preserveAspectRatio="none" height="10"><path d="M0 8 Q50 -2 100 8 V20 H0Z" fill="var(--blue)"/></svg>
</div>

<!-- envelopes -->
<div class="piece envelope" style="left:672px;top:88px">
  <svg class="flap" viewBox="0 0 100 34" preserveAspectRatio="none"><path d="M0 0 H100 V6 L50 22 L0 6Z" fill="var(--green)"/><path d="M0 6 L50 22 L100 6" fill="none" stroke="var(--blue)" stroke-width=".8"/></svg>
</div>
<div class="piece envelope" style="left:690px;top:136px">
  <div class="wordmark"><span class="dot"></span><span class="name">Larkspur Valley Wellness</span></div>
  <div class="small" style="position:absolute;left:6px;top:16px">418 Quarry Lane<br>Phillipsburg, KS 67492-2741</div>
  <svg class="wave" viewBox="0 0 100 20" preserveAspectRatio="none" height="8"><path d="M0 10 Q50 0 100 10 V20 H0Z" fill="var(--blue)"/></svg>
</div>

<!-- folder closed -->
<div class="piece folder closed" style="left:866px">
  <svg class="wave" viewBox="0 0 100 100" preserveAspectRatio="none" height="185" style="top:0"><path d="M0 40 Q50 60 100 40" fill="none" stroke="var(--paper)" stroke-opacity=".35" stroke-width="1"/></svg>
  <div class="wordmark"><span class="dot"></span><span class="name">Larkspur Valley Wellness</span></div>
</div>

<!-- folder open -->
<div class="piece folder open" style="left:1006px">
  <svg class="pocket" viewBox="0 0 100 30" preserveAspectRatio="none"><path d="M0 6 Q25 -2 50 6 V30 H0Z" fill="var(--blue)"/><path d="M50 6 Q75 -2 100 6 V30 H50Z" fill="var(--blue-deep)" opacity=".15"/></svg>
  <div class="pocket-card">
    <div class="wordmark"><span class="dot"></span><span class="name">Larkspur Valley Wellness</span></div>
  </div>
</div>

</body>
</html>
```